Graphic of a Book Cover that I am launching

Title of the Book is: Relapse Rally
Subtitle: 9 Steps to hold steady, push onward, and outlast the storm again like our family did
Author Name: Toma Verlund
(Below are thoughts on design work: Lighter background, picture of a boxing ring (black), gloves (red), and belt showing 4 time champion...
Serious facing and professional looking cover.)

Target Market(s)

Newly Diagnosed Cancer Patients and Family

Industry/Entity Type

Medical And Science

Font styles to use
Sans Serif

Colors
f04a50
ffffff
000000

Requirements
Must have
• Well Designed book cover
Nice to have
• Lighter background, picture of a boxing ring (black), gloves (red), and belt showing 4 time champion...
• Serious facing and professional looking cover.
Should not have
• cartoon animations

```html
<!DOCTYPE html>
<html lang="en">
<head>
<meta charset="utf-8">
<title>Relapse Rally — Book Cover</title>
<link rel="stylesheet" href="https://fonts.googleapis.com/css2?family=Oswald:wght@700&family=Roboto+Condensed:wght@700&family=Montserrat:wght@700&display=swap">
<style>
  :root {
    --brand-red: #f04a50;
    --brand-red-deep: #b92f35;
    --ink: #1b1b1b;
    --paper: #ffffff;
    --ring-light: #f4f5f7;
    --ring-mid: #c3c7cd;
    --ring-dark: #3e4654;
    --stage: #dcdcdc;
  }
  html, body {
    margin: 0;
    width: 1200px;
    height: 1200px;
    overflow: hidden;
    background: var(--stage);
  }
  .stage {
    width: 1200px;
    height: 1200px;
    display: flex;
    align-items: center;
    justify-content: center;
  }
  .book-cover {
    width: 802px;
    height: 1120px;
    display: block;
    box-shadow: 0 18px 40px rgba(0,0,0,0.28);
  }
  .title-main { font-family: "Oswald", sans-serif; font-weight: 700; font-size: 120px; letter-spacing: 6px; fill: var(--brand-red); }
  .title-box-word { font-family: "Oswald", sans-serif; font-weight: 700; font-size: 96px; letter-spacing: 1px; fill: var(--ink); text-anchor: middle; }
  .subtitle { font-family: "Roboto Condensed", sans-serif; font-weight: 700; font-size: 54px; text-anchor: middle; }
  .subtitle .light { fill: var(--paper); }
  .subtitle .dark { fill: var(--ink); }
  .author { font-family: "Montserrat", sans-serif; font-weight: 700; font-size: 40px; letter-spacing: 14px; fill: var(--paper); text-anchor: middle; }
</style>
</head>
<body>
<main class="stage">
  <svg class="book-cover" viewBox="0 0 875 1222" xmlns="http://www.w3.org/2000/svg" aria-label="Book cover: Relapse Rally by Toma Verlund">
    <defs>
      <linearGradient id="ringTone" x1="0" y1="0" x2="0" y2="1">
        <stop offset="0" stop-color="var(--ring-light)"/>
        <stop offset="0.4" stop-color="#e9ebee"/>
        <stop offset="0.62" stop-color="var(--ring-mid)"/>
        <stop offset="0.8" stop-color="#6b7482"/>
        <stop offset="1" stop-color="var(--ring-dark)"/>
      </linearGradient>
      <radialGradient id="ringGlow" cx="0.5" cy="0.35" r="0.55">
        <stop offset="0" stop-color="#ffffff" stop-opacity="0.8"/>
        <stop offset="1" stop-color="#ffffff" stop-opacity="0"/>
      </radialGradient>
      <radialGradient id="gloveTone" cx="0.5" cy="0.5" r="0.5">
        <stop offset="0" stop-color="var(--brand-red-deep)" stop-opacity="0.55"/>
        <stop offset="0.7" stop-color="var(--brand-red-deep)" stop-opacity="0.25"/>
        <stop offset="1" stop-color="var(--brand-red-deep)" stop-opacity="0"/>
      </radialGradient>
    </defs>

    <!-- cover base -->
    <rect class="cover-base" x="0" y="0" width="875" height="1222" fill="var(--brand-red)"/>

    <!-- gloves photo area -->
    <g class="gloves-photo" role="img" aria-label="Photo of two red boxing gloves touching">
      <ellipse cx="170" cy="1000" rx="260" ry="150" fill="url(#gloveTone)"/>
      <ellipse cx="705" cy="1000" rx="260" ry="150" fill="url(#gloveTone)"/>
    </g>

    <!-- boxing ring photo area -->
    <g class="ring-photo" role="img" aria-label="Photo of an empty white boxing ring corner with grey ropes">
      <polygon points="0,347 875,272 875,765 437,847 0,765" fill="url(#ringTone)"/>
      <polygon points="0,347 875,272 875,765 437,847 0,765" fill="url(#ringGlow)"/>
    </g>

    <!-- slanted title band -->
    <polygon class="title-band" points="0,150 875,60 875,272 0,347" fill="var(--ink)"/>

    <g class="title" transform="rotate(-5.9 437 211)">
      <text class="title-main" x="52" y="262">RELAPSE</text>
      <rect class="title-box" x="556" y="142" width="262" height="130" fill="var(--brand-red)"/>
      <text class="title-box-word" x="687" y="246">RALLY</text>
    </g>

    <!-- subtitle -->
    <text class="subtitle" x="437" y="902"><tspan class="light">9 STEPS TO </tspan><tspan class="dark">HOLD STEADY</tspan></text>
    <text class="subtitle" x="437" y="956"><tspan class="light">PUSH </tspan><tspan class="dark">ONWARD</tspan></text>
    <text class="subtitle" x="437" y="1010"><tspan class="light">AND OUTLAST </tspan><tspan class="dark">THE STORM</tspan></text>
    <text class="subtitle" x="437" y="1064"><tspan class="light">AGAIN </tspan><tspan class="dark">LIKE OUR</tspan></text>
    <text class="subtitle" x="437" y="1118"><tspan class="light">FAMILY </tspan><tspan class="dark">DID</tspan></text>

    <!-- author band -->
    <rect class="author-band" x="0" y="1152" width="875" height="70" fill="var(--ink)"/>
    <text class="author" x="437" y="1202">TOMA VERLUND</text>
  </svg>
</main>
</body>
</html>
```